Printing Business Card

I would like the colorful accents of my business to match with an artistic design. The idea is that I would like to have a creative mix so that I am making a embossed, suede card to show off with marketing events.

```html
<!DOCTYPE html>
<html lang="en">
<head>
<meta charset="utf-8">
<title>Keystone Print Co. – Business Card</title>
<link href="https://fonts.googleapis.com/css2?family=Arimo:wght@400;700&display=swap" rel="stylesheet">
<style>
  :root {
    --backdrop: #4a4a4c;
    --card-white: #ffffff;
    --card-black: #1c1c1d;
    --ink: #555555;
    --cyan: #1a97e0;
    --magenta: #dc1a7f;
    --yellow: #f2c21b;
    --red: #f20d0d;
    --blue: #0a0fbf;
    --divider: #e4e4e4;
  }
  * { box-sizing: border-box; margin: 0; padding: 0; }
  html, body {
    width: 1200px; height: 960px; overflow: hidden;
    background: var(--backdrop);
    font-family: "Arimo", Arial, sans-serif;
  }
  .sheet {
    width: 1200px; height: 960px;
    display: flex; flex-direction: column; align-items: center;
    justify-content: center; gap: 30px;
  }
  .card {
    width: 770px; height: 440px; position: relative; overflow: hidden;
    box-shadow: 0 10px 28px rgba(0,0,0,.45);
  }
  /* Back side */
  .card--back {
    background: var(--card-black);
    display: flex; align-items: center; justify-content: center; gap: 18px;
  }
  .card--back .brand-dot {
    width: 26px; height: 26px; border-radius: 50%; background: #ffffff;
  }
  .card--back .brand-name {
    color: #ffffff; font-weight: 700; font-size: 46px; letter-spacing: .5px;
  }
  /* Front side */
  .card--front { background: var(--card-white); }
  .brand {
    position: absolute; left: 0; top: 0; width: 440px; height: 418px;
    display: flex; align-items: center; justify-content: center; gap: 12px;
  }
  .brand .brand-dot {
    width: 22px; height: 22px; border-radius: 50%; background: var(--cyan);
  }
  .brand .brand-name {
    color: #111111; font-weight: 700; font-size: 34px;
  }
  .divider {
    position: absolute; left: 450px; top: 60px; width: 1px; height: 300px;
    background: var(--divider);
  }
  .contact {
    position: absolute; left: 478px; top: 78px; color: var(--ink);
  }
  .contact__name {
    color: var(--cyan); font-weight: 700; font-size: 25px; text-transform: uppercase;
  }
  .contact__role { color: var(--magenta); font-size: 17px; margin-top: 4px; }
  .contact__address { font-size: 17px; line-height: 22px; margin-top: 12px; margin-left: 14px; }
  .contact__list { list-style: none; margin-top: 12px; margin-left: 24px; }
  .contact__list li {
    display: flex; align-items: center; gap: 12px;
    font-size: 17px; line-height: 23px;
  }
  .contact__list svg { width: 14px; height: 14px; flex: none; fill: var(--cyan); }
  .colour-band {
    position: absolute; left: 0; right: 0; bottom: 0; height: 22px; display: flex;
  }
  .colour-band span { flex: 1; }
  .colour-band .cyan { background: var(--cyan); }
  .colour-band .magenta { background: var(--magenta); }
  .colour-band .yellow { background: var(--yellow); }
  .colour-band .red { background: var(--red); }
  .colour-band .blue { background: var(--blue); }
</style>
</head>
<body>
<main class="sheet">
  <section class="card card--back" aria-label="Card back">
    <span class="brand-dot"></span>
    <span class="brand-name">Keystone Print Co.</span>
  </section>

  <section class="card card--front" aria-label="Card front">
    <div class="brand">
      <span class="brand-dot"></span>
      <span class="brand-name">Keystone Print Co.</span>
    </div>
    <div class="divider"></div>
    <div class="contact">
      <h1 class="contact__name">Daniel Reyes</h1>
      <p class="contact__role">President</p>
      <p class="contact__address">412 Birchwood Avenue<br>Fairbanks, Alaska 99701</p>
      <ul class="contact__list">
        <li>
          <svg viewBox="0 0 16 16" aria-hidden="true"><path d="M3 1l3 3-1.5 2c1 2 3 4 5 5L11.5 9.5l3 3-2 2.5C6 15 1 10 .5 3.5z"/></svg>
          555-204-7731
        </li>
        <li>
          <svg viewBox="0 0 16 16" aria-hidden="true"><path d="M4 0h8a1 1 0 0 1 1 1v14a1 1 0 0 1-1 1H4a1 1 0 0 1-1-1V1a1 1 0 0 1 1-1zm1 2v10h6V2zm3 11a1 1 0 1 0 0 2 1 1 0 0 0 0-2z"/></svg>
          555-318-6402
        </li>
        <li>
          <svg viewBox="0 0 16 16" aria-hidden="true"><path d="M4 0h8v5H4zM1 6h14v7h-2v3H3v-3H1zm4 5v3h6v-3z"/></svg>
          555-476-1290
        </li>
        <li>
          <svg viewBox="0 0 16 16" aria-hidden="true"><path d="M0 3h16v10H0zm1.5 1.5L8 9l6.5-4.5v-.5h-13z"/></svg>
          hello@keystoneprint.com
        </li>
        <li>
          <svg viewBox="0 0 16 16" aria-hidden="true"><circle cx="8" cy="8" r="7.5"/></svg>
          www.keystoneprint.com
        </li>
      </ul>
    </div>
    <div class="colour-band">
      <span class="cyan"></span><span class="magenta"></span><span class="yellow"></span><span class="red"></span><span class="blue"></span>
    </div>
  </section>
</main>
</body>
</html>
```